Yard Sign Design for luxury design & build company

Looking to have 18" x 24" company yard signs designed.
An update to the business logo might be helpful.
Photos are not necessary but use if you can make inspiring.

Industry: Construction

Looking for a large headline of "Basement Finishing"
Website: www.tamberlyhomes.com
Phone Number (612) 555-0174
FB link: facebook.com/tamberlyhomesmn
Instagram: www.instagram.com/tamberlyhomesmn

Industry/Entity Type

Construction

Colors

Designer to choose colors to be used in the design.

Requirements
Must have
• Impactful high end characteristics
Nice to have
• Depth and detail graphis

```html
<!DOCTYPE html>
<html lang="en">
<head>
<meta charset="utf-8">
<title>Tamberly Homes — Basement Finishing Yard Sign</title>
<link rel="stylesheet" href="https://fonts.googleapis.com/css2?family=Poppins:wght@600;700;900&family=Orbitron:wght@600&family=Oswald:wght@500&display=swap">
<style>
  :root {
    --backdrop: #c9c9c9;
    --sign-white: #ffffff;
    --ink: #1e1e1e;
    --steel: #6e6e6e;
    --brand-red: #c8190f;
    --brand-red-deep: #8e0e08;
    --night: #141414;
    --night-soft: #2c2c2c;
    --star: #f6b813;
    --text-light: #ffffff;
  }
  * { box-sizing: border-box; margin: 0; padding: 0; }
  html, body { width: 773px; height: 1200px; overflow: hidden; }
  body { background: var(--backdrop); font-family: "Poppins", sans-serif; position: relative; }

  .yard-sign {
    position: absolute; left: 36px; top: 337px; width: 700px; height: 525px;
    background: var(--sign-white);
    box-shadow: 0 10px 28px rgba(0,0,0,.35);
    overflow: hidden;
  }
  .headline {
    position: absolute; left: 0; top: 0; width: 100%; height: 249px;
    font-weight: 900; text-align: center; line-height: 1;
  }
  .headline-line {
    position: absolute; left: 0; width: 100%; font-size: 103px; letter-spacing: -1px;
  }
  .headline-line.primary { top: 32px; color: var(--ink); }
  .headline-line.secondary { top: 125px; color: var(--steel); }

  .phone-band {
    position: absolute; left: 0; top: 249px; width: 100%; height: 97px;
    background: linear-gradient(180deg, var(--brand-red) 0%, #b3140b 60%, var(--brand-red-deep) 100%);
  }
  .phone-icon { position: absolute; left: 58px; top: 20px; width: 58px; height: 58px; }
  .phone-number {
    position: absolute; left: 128px; top: 14px;
    font-family: "Orbitron", sans-serif; font-weight: 600; font-size: 58px;
    color: var(--text-light); letter-spacing: 0; white-space: nowrap; line-height: 1.15;
  }

  .info-band {
    position: absolute; left: 0; top: 346px; width: 100%; height: 179px;
    background: radial-gradient(ellipse at 40% 30%, var(--night-soft) 0%, var(--night) 75%);
  }
  .brand-mark {
    position: absolute; left: 45px; top: 35px; width: 88px; height: 88px;
    border-radius: 50%; border: 3px solid var(--brand-red);
  }
  .brand-name {
    position: absolute; left: 140px; top: 58px;
    font-weight: 600; font-size: 25px; color: var(--text-light);
    letter-spacing: 1.5px; line-height: 1.05; white-space: nowrap;
  }

  .review {
    position: absolute; left: 330px; top: 28px; color: var(--text-light);
  }
  .review-badge {
    position: absolute; left: 4px; top: 2px; width: 28px; height: 28px;
    border-radius: 50%; background: #e8e8e8;
  }
  .review-label {
    position: absolute; left: 38px; top: 0; font-weight: 700; font-size: 12.5px;
    line-height: 1.2; white-space: nowrap;
  }
  .review-score {
    position: absolute; left: 0; top: 34px; font-weight: 700; font-size: 21px;
    white-space: nowrap; line-height: 1;
  }
  .review-score .stars { color: var(--star); font-size: 19px; letter-spacing: 1px; }

  .social {
    position: absolute; left: 503px; top: 32px;
  }
  .social-dot {
    position: absolute; top: 0; width: 22px; height: 22px; border-radius: 50%;
  }
  .social-dot.one { left: 0; background: #1877f2; }
  .social-dot.two { left: 30px; background: #e1306c; }
  .social-handle {
    position: absolute; left: 0; top: 30px;
    font-family: "Oswald", sans-serif; font-weight: 500; font-size: 18px;
    color: var(--text-light); white-space: nowrap; letter-spacing: -.3px;
  }

  .website {
    position: absolute; right: 40px; top: 92px;
    font-weight: 600; font-size: 21px; color: var(--text-light); white-space: nowrap;
  }
  .website .domain { color: var(--brand-red); }
</style>
</head>
<body>
  <main class="yard-sign">
    <header class="headline">
      <div class="headline-line primary">BASEMENT</div>
      <div class="headline-line secondary">FINISHING</div>
    </header>

    <section class="phone-band" role="img" aria-label="Red-toned photo of a finished basement interior behind the phone number">
      <svg class="phone-icon" viewBox="0 0 58 58" aria-hidden="true">
        <circle cx="29" cy="29" r="26" fill="#000" stroke="#fff" stroke-width="5"/>
        <path d="M20 17c2-1 4 0 5 2l2 5c.5 1.5 0 3-1.5 4l-1.5 1c1 3 4 6 7 7l1-1.5c1-1.5 2.5-2 4-1.5l5 2c2 1 3 3 2 5l-1 2c-1 2-3 3-5 3C25 42 16 33 16 21c0-2 1-4 3-5z" fill="#fff"/>
      </svg>
      <div class="phone-number">(612) 555-0174</div>
    </section>

    <section class="info-band" role="img" aria-label="Dark monochrome photo of a furnished basement lounge">
      <div class="brand-mark"></div>
      <div class="brand-name">TAMBERLY<br>HOMES</div>

      <div class="review">
        <div class="review-badge"></div>
        <div class="review-label">HomeRate<br>Review</div>
        <div class="review-score">5.0<span class="stars">★★★★★</span></div>
      </div>

      <div class="social">
        <div class="social-dot one"></div>
        <div class="social-dot two"></div>
        <div class="social-handle">@TAMBERLYHOMESMN</div>
      </div>

      <div class="website">www.<span class="domain">tamberlyhomes</span>.com</div>
    </section>
  </main>
</body>
</html>
```